Moonvale Jewellery Limited - designer pearl and silver jewellery

Designer silver jewellery with a twist that 20% of the net profit will be donated to a charity in India to help abused children

The products are designed to make the wearer not only feel good about how good the jewellery looks but to know they are also helping others less fortunate

All the Jewellery is designed by myself Margaret Doyle and made in 925 Hallmarked sterling silver . The hallmarking is carried out by the Corrick Assay office

This is my first website and will need to be suitable for e-commerce

Target Market(s)

Stylish women with a love of simple and elegant design , not high fashion by timeless simplicity

Number of Pages Required

5+ page

Font styles to use
Sans Serif

Colors
e666a6

Requirements
Must have
• Reference to Sterling silver
• The Pantone ref for my logo background now is white out of 2063
Nice to have
• Fresh and contemporary - Aimed at 25-55 market
• The same consumer would
• Like this product as likes Velmira, Kester Dunne but will also appreciate the fact this product is about helping others as well
• The Jewellery is about clean simple lines , elegance , hand made and styled to be timeless
• The products are designed to be casual and elegant and all feature either natural freshwater pearls or semi precious gemstones
• I also would like a page that customers can arrange to book talks about the design and production of the product . I give these talks generally tomladies groups and explain the manufacturing process and what the charity I’m doing supports

```html
<!DOCTYPE html>
<html lang="en">
<head>
<meta charset="utf-8">
<title>Moonvale Jewellery Limited – Website Pages</title>
<link rel="stylesheet" href="https://fonts.googleapis.com/css2?family=Montserrat:wght@400;500;600;700&family=Open+Sans:wght@400;600&display=swap">
<style>
  :root {
    --pink: #e666a6;
    --pink-deep: #e33a6e;
    --pink-soft: #f7dbe7;
    --blush: #efe2da;
    --stage: #e8e8ea;
    --page: #ffffff;
    --panel: #f1f1f3;
    --ink: #3a3a40;
    --muted: #8d8d95;
    --line: #e4e4e8;
    --silver-a: #fbfbfc;
    --silver-b: #d6d7dc;
    --title: "Montserrat", sans-serif;
    --body: "Open Sans", sans-serif;
  }
  * { box-sizing: border-box; margin: 0; padding: 0; }
  html, body { width: 1200px; height: 789px; overflow: hidden; }
  body { background: var(--stage); font-family: var(--body); color: var(--ink); }

  .board { display: flex; gap: 18px; padding: 24px; height: 789px; }
  .page {
    width: 372px; height: 741px; background: var(--page);
    box-shadow: 0 6px 18px rgba(0,0,0,.08); overflow: hidden;
    display: flex; flex-direction: column;
  }

  /* shared */
  .section-title { font-family: var(--title); font-weight: 600; color: var(--pink-deep); text-align: center; font-size: 12px; }
  .rule { width: 34px; height: 2px; background: var(--pink); margin: 5px auto 0; }
  .product-photo { background: linear-gradient(145deg, var(--silver-a), #eceef1 55%, var(--silver-b)); border-radius: 3px; }
  .btn-pink { display: inline-block; background: var(--pink-deep); color: #fff; font-family: var(--title); font-size: 7px; letter-spacing: .08em; padding: 5px 12px; border-radius: 2px; }
  .btn-outline { display: inline-block; border: 1px solid var(--pink-deep); color: var(--pink-deep); font-family: var(--title); font-size: 7px; letter-spacing: .08em; padding: 5px 12px; }
  .product-name { font-family: var(--title); font-size: 6.5px; font-weight: 600; letter-spacing: .06em; text-transform: uppercase; }
  .product-price { font-size: 6px; color: var(--pink-deep); margin-top: 2px; }
  .small-caption { font-size: 6.5px; color: var(--muted); letter-spacing: .05em; }
  .big-pink { font-family: var(--title); font-size: 17px; color: var(--pink-deep); font-weight: 500; margin-top: 4px; }

  /* home page */
  .site-header { display: flex; align-items: center; justify-content: space-between; padding: 10px 14px 7px; }
  .brand { display: flex; align-items: center; gap: 5px; font-family: var(--title); font-weight: 600; font-size: 10px; color: var(--pink-deep); }
  .brand-dot { width: 10px; height: 10px; border-radius: 50%; background: var(--pink); }
  .utility { display: flex; gap: 7px; font-size: 6px; color: var(--muted); }
  .main-nav { display: flex; gap: 13px; padding: 4px 14px; border-top: 1px solid var(--line); border-bottom: 1px solid var(--line); font-family: var(--title); font-size: 6px; color: var(--muted); align-items: center; }
  .main-nav .active { background: var(--pink-deep); color: #fff; padding: 2px 6px; }
  .hero { position: relative; height: 220px; background: linear-gradient(90deg, #e9dbd2, var(--blush) 55%, #f4ece7); }
  .hero-photo { position: absolute; right: 0; top: 0; width: 150px; height: 100%; background: linear-gradient(160deg, #f3e7e2, #dcc4bb 60%, #ecd8d4); }
  .hero-copy { position: absolute; left: 30px; width: 190px; top: 78px; text-align: center; }
  .hero-kicker { font-family: var(--title); font-size: 7.5px; letter-spacing: .1em; color: var(--ink); }
  .hero-headline { font-family: var(--title); font-size: 12px; font-weight: 600; color: var(--pink-deep); margin: 5px 0 9px; }

  .trending { background: var(--panel); padding: 16px 14px 16px; }
  .product-grid { display: grid; grid-template-columns: repeat(4, 1fr); gap: 8px; margin-top: 12px; }
  .product-card { background: #fff; padding: 7px 7px 8px; text-align: center; height: 124px; display: flex; flex-direction: column; align-items: center; }
  .product-card .product-photo { width: 100%; height: 82px; margin-bottom: 7px; }

  .collection-intro { flex: 1; display: flex; flex-direction: column; justify-content: center; text-align: center; padding: 0 14px; }

  /* collection page */
  .collection-hero { position: relative; height: 150px; background: linear-gradient(180deg, #fbf7f9, #f6eef2); text-align: center; padding-top: 32px; }
  .collection-hero .big-pink { font-size: 15px; }
  .hero-sub { font-size: 6px; color: var(--muted); margin: 5px 0 12px; }
  .hero-trinket { position: absolute; right: 44px; top: 44px; width: 36px; height: 22px; border-radius: 40%; background: radial-gradient(circle, #e3c8a3, #b48c70); }
  .new-collections { padding: 14px 14px 0; }
  .mosaic { display: grid; grid-template-columns: 1.3fr 1fr; grid-template-rows: 78px 96px 96px; gap: 4px; margin-top: 12px; }
  .tile { position: relative; }
  .tile-caption { position: absolute; left: 8px; bottom: 7px; font-family: var(--title); font-size: 6.5px; color: #fff; font-weight: 600; }
  .tile-wide { grid-column: 1; grid-row: 1; background: linear-gradient(135deg, #f5f3f4, #e6ddd8); }
  .tile-light { grid-column: 2; grid-row: 1; background: linear-gradient(135deg, #f1eef4, #d9e2ec); }
  .tile-pink { grid-column: 1; grid-row: 2 / 4; background: linear-gradient(135deg, #f26b9a, #e94f86 60%, #c9d2da); }
  .tile-dark { grid-column: 2; grid-row: 2 / 4; background: linear-gradient(160deg, #d9c6b5, #4b3b35 55%, #a0796a); }
  .bestsellers { flex: 1; padding: 18px 14px 16px; border-top: 1px solid var(--line); margin-top: 20px; display: flex; flex-direction: column; }
  .product-row { display: flex; justify-content: space-between; margin-top: 14px; }
  .row-item { width: 60px; text-align: center; }
  .row-item .product-photo { width: 54px; height: 54px; margin: 0 auto 6px; }
  .bestsellers .product-row { flex: 1; align-items: center; }
  .bestsellers .row-item .product-photo { height: 74px; }
  .collection-foot { height: 26px; background: var(--panel); }

  /* reviews page */
  .best-block { padding: 18px 14px 16px; }
  .best-block .section-title { text-align: left; }
  .best-box { border: 1px solid var(--line); padding: 12px 8px 10px; margin-top: 10px; }
  .pink-line { height: 2px; background: var(--pink-soft); }
  .testimonials { background: var(--panel); padding: 22px 16px 22px; text-align: center; }
  .testi-title { font-family: var(--title); font-size: 8.5px; letter-spacing: .06em; font-weight: 600; }
  .testi-text { font-size: 6px; color: var(--muted); line-height: 1.6; margin: 7px auto 0; max-width: 300px; }
  .testi-author { font-size: 6px; color: var(--pink-deep); margin-top: 5px; }
  .quote-row { display: flex; align-items: center; gap: 8px; margin-top: 16px; text-align: left; }
  .quote-mark { font-family: var(--title); font-size: 18px; color: var(--ink); }
  .quote-text { font-size: 6.5px; line-height: 1.6; flex: 1; }
  .avatar-row { display: flex; justify-content: center; align-items: flex-end; gap: 22px; margin-top: 18px; }
  .avatar { text-align: center; }
  .avatar-photo { width: 26px; height: 26px; border-radius: 50%; background: linear-gradient(135deg, #e9d2c4, #b99a8a); margin: 0 auto 4px; }
  .avatar-photo.lead { width: 34px; height: 34px; }
  .stars { font-size: 6.5px; color: var(--pink-deep); letter-spacing: 1px; }
  .site-footer { display: grid; grid-template-columns: 1.3fr 1fr 1fr 1fr 1fr; gap: 8px; padding: 24px 14px 14px; flex: 1; align-content: start; }
  .footer-head { font-family: var(--title); font-size: 6.5px; font-weight: 600; letter-spacing: .06em; text-transform: uppercase; margin-bottom: 7px; }
  .footer-list { list-style: none; font-size: 6px; color: var(--muted); line-height: 2.1; }
  .footer-contact { font-size: 6px; color: var(--muted); line-height: 1.8; }
  .phone { display: flex; align-items: center; gap: 4px; margin-top: 8px; font-size: 6.5px; color: var(--ink); font-weight: 600; }
  .bottom-bar { background: var(--pink-deep); color: #fff; text-align: center; font-size: 6px; letter-spacing: .08em; padding: 10px 0; }
</style>
</head>
<body>
<main class="board">

  <section class="page page-home">
    <header class="site-header">
      <div class="brand"><span class="brand-dot"></span>Moonvale Jewellery</div>
      <div class="utility"><span>Login</span><span>Wishlist</span><span>Cart (0)</span></div>
    </header>
    <nav class="main-nav">
      <span class="active">HOME</span><span>SHOP</span><span>RINGS</span><span>EARRINGS</span><span>NECKLACES</span><span>TALKS</span><span>CONTACT</span>
    </nav>
    <div class="hero">
      <div class="hero-photo" role="img" aria-label="Model in soft pink tones holding a bouquet of roses"></div>
      <div class="hero-copy">
        <p class="hero-kicker">"TRADITIONAL ENGLISH JEWELLERY"</p>
        <p class="hero-headline">NEW COLLECTIONS</p>
        <span class="btn-pink">SHOP NOW</span>
      </div>
    </div>
    <div class="trending">
      <h2 class="section-title">Trending Products</h2>
      <div class="rule"></div>
      <div class="product-grid">
        <div class="product-card"><div class="product-photo" role="img" aria-label="Freshwater pearl stud earrings"></div><p class="product-name">Earrings</p><p class="product-price">£45.00</p></div>
        <div class="product-card"><div class="product-photo" role="img" aria-label="Sterling silver ring"></div><p class="product-name">Rings</p><p class="product-price">£38.00</p></div>
        <div class="product-card"><div class="product-photo" role="img" aria-label="Silver heart pendant necklace"></div><p class="product-name">Necklaces</p><p class="product-price">£52.00</p></div>
        <div class="product-card"><div class="product-photo" role="img" aria-label="Silver bracelet"></div><p class="product-name">Bracelets</p><p class="product-price">£60.00</p></div>
        <div class="product-card"><div class="product-photo" role="img" aria-label="Silver pendant on chain"></div><p class="product-name">Pendants</p><p class="product-price">£42.00</p></div>
        <div class="product-card"><div class="product-photo" role="img" aria-label="Silver hoop earrings"></div><p class="product-name">Earrings</p><p class="product-price">£40.00</p></div>
        <div class="product-card"><div class="product-photo" role="img" aria-label="Dark pearl stud earrings"></div><p class="product-name">Studs</p><p class="product-price">£35.00</p></div>
        <div class="product-card"><div class="product-photo" role="img" aria-label="Silver gemstone ring"></div><p class="product-name">Rings</p><p class="product-price">£48.00</p></div>
      </div>
    </div>
    <div class="collection-intro">
      <p class="small-caption">Sterling Silver &amp; Pearls</p>
      <h2 class="big-pink">New Trending Collection</h2>
    </div>
  </section>

  <section class="page page-collection">
    <div class="collection-hero">
      <p class="small-caption">Hallmarked 925 Sterling Silver</p>
      <h2 class="big-pink">New Trending Collection</h2>
      <p class="hero-sub">Handmade pieces with timeless, simple lines</p>
      <span class="btn-outline">SHOP NOW</span>
      <div class="hero-trinket" role="img" aria-label="Gold and pearl earrings on display"></div>
    </div>
    <div class="new-collections">
      <h2 class="section-title">New Collections</h2>
      <div class="rule"></div>
      <div class="mosaic">
        <div class="tile tile-wide" role="img" aria-label="Pearl earrings on white silk"></div>
        <div class="tile tile-light" role="img" aria-label="Silver rings on pale fabric"></div>
        <div class="tile tile-pink" role="img" aria-label="Gemstone drop earrings on pink background"><span class="tile-caption">Gemstone Earrings</span></div>
        <div class="tile tile-dark" role="img" aria-label="Gold and pearl jewellery laid on a wooden tray"><span class="tile-caption">Pearl Sets</span></div>
      </div>
    </div>
    <div class="bestsellers">
      <h2 class="section-title">Bestselling Products</h2>
      <div class="rule"></div>
      <div class="product-row">
        <div class="row-item"><div class="product-photo" role="img" aria-label="Silver hoop earrings"></div><p class="product-name">Earrings</p><p class="product-price">£40.00</p></div>
        <div class="row-item"><div class="product-photo" role="img" aria-label="Silver ring"></div><p class="product-name">Rings</p><p class="product-price">£38.00</p></div>
        <div class="row-item"><div class="product-photo" role="img" aria-label="Pearl studs"></div><p class="product-name">Studs</p><p class="product-price">£35.00</p></div>
        <div class="row-item"><div class="product-photo" role="img" aria-label="Silver ring with stone"></div><p class="product-name">Rings</p><p class="product-price">£48.00</p></div>
        <div class="row-item"><div class="product-photo" role="img" aria-label="Silver bracelet"></div><p class="product-name">Bracelets</p><p class="product-price">£60.00</p></div>
      </div>
    </div>
    <div class="collection-foot"></div>
  </section>

  <section class="page page-reviews">
    <div class="best-block">
      <h2 class="section-title">Bestselling Products</h2>
      <div class="best-box product-row">
        <div class="row-item"><div class="product-photo" role="img" aria-label="Silver hoop earrings"></div><p class="product-name">Earrings</p><p class="product-price">£40.00</p></div>
        <div class="row-item"><div class="product-photo" role="img" aria-label="Silver ring"></div><p class="product-name">Rings</p><p class="product-price">£38.00</p></div>
        <div class="row-item"><div class="product-photo" role="img" aria-label="Pearl studs"></div><p class="product-name">Studs</p><p class="product-price">£35.00</p></div>
        <div class="row-item"><div class="product-photo" role="img" aria-label="Silver drop earrings"></div><p class="product-name">Earrings</p><p class="product-price">£44.00</p></div>
        <div class="row-item"><div class="product-photo" role="img" aria-label="Silver bracelet"></div><p class="product-name">Bracelets</p><p class="product-price">£60.00</p></div>
      </div>
    </div>
    <div class="pink-line"></div>
    <div class="testimonials">
      <h2 class="testi-title">100% WORDS FROM OUR CUSTOMERS</h2>
      <p class="testi-text">Every piece feels special, and knowing part of each sale helps children in need makes wearing it even better.</p>
      <p class="testi-author">Happy Client</p>
      <div class="quote-row">
        <span class="quote-mark">“</span>
        <p class="quote-text">Simple, elegant and beautifully made. My pearl earrings go with everything I own.</p>
        <span class="quote-mark">”</span>
      </div>
      <div class="avatar-row">
        <div class="avatar"><div class="avatar-photo lead" role="img" aria-label="Customer portrait"></div><span class="stars">★★★★★</span></div>
        <div class="avatar"><div class="avatar-photo" role="img" aria-label="Customer portrait"></div><span class="stars">★★★★★</span></div>
        <div class="avatar"><div class="avatar-photo" role="img" aria-label="Customer portrait"></div><span class="stars">★★★★★</span></div>
        <div class="avatar"><div class="avatar-photo" role="img" aria-label="Customer portrait"></div><span class="stars">★★★★★</span></div>
        <div class="avatar"><div class="avatar-photo" role="img" aria-label="Customer portrait"></div><span class="stars">★★★★★</span></div>
      </div>
    </div>
    <footer class="site-footer">
      <div>
        <p class="footer-head">Moonvale</p>
        <p class="footer-contact">Handmade silver and pearl jewellery, hallmarked by the Corrick Assay office.</p>
        <p class="footer-contact">hello@moonvale.example</p>
        <p class="phone">
          <svg width="8" height="8" viewBox="0 0 24 24" aria-hidden="true"><path fill="var(--ink)" d="M6.6 10.8a15 15 0 0 0 6.6 6.6l2.2-2.2c.3-.3.7-.4 1-.2 1.1.4 2.3.6 3.6.6.6 0 1 .4 1 1V20c0 .6-.4 1-1 1A17 17 0 0 1 3 4c0-.6.4-1 1-1h3.5c.6 0 1 .4 1 1 0 1.3.2 2.5.6 3.6.1.3 0 .7-.2 1z"/></svg>
          01632 960 418
        </p>
      </div>
      <div><p class="footer-head">Shop</p><ul class="footer-list"><li>Rings</li><li>Earrings</li><li>Necklaces</li><li>Bracelets</li></ul></div>
      <div><p class="footer-head">Categories</p><ul class="footer-list"><li>Pearls</li><li>Gemstones</li><li>Sterling Silver</li><li>Gift Sets</li></ul></div>
      <div><p class="footer-head">Useful</p><ul class="footer-list"><li>Book a Talk</li><li>Our Charity</li><li>Delivery</li><li>Returns</li></ul></div>
      <div><p class="footer-head">Contact</p><ul class="footer-list"><li>About Us</li><li>Contact</li><li>FAQ</li><li>Terms</li></ul></div>
    </footer>
    <div class="bottom-bar">© 2024 MOONVALE JEWELLERY LIMITED</div>
  </section>

</main>
</body>
</html>
```